Product Setup Instructional Infographic/flyer

Converting product instructions into an infographic. Would prefer that the instructions fit on a 4x6 card, front and back, but a slightly larger size is acceptable as well.

Logo Text

Harbor Crest (Rebranding just as Harbor Crest, instead of Harbor Crest)

Font styles to use
Decorative

Colors

Designer to choose colors to be used in the design.

Requirements
Must have
• NA
Nice to have
• NA
Should not have
• NA

```html
<!DOCTYPE html>
<html lang="en">
<head>
<meta charset="utf-8">
<title>Harbor Crest – How to Cure Your Oak Barrel</title>
<link href="https://fonts.googleapis.com/css2?family=Oswald:wght@500;600&family=Open+Sans:wght@400;600&display=swap" rel="stylesheet">
<style>
  :root {
    --page: #ffffff;
    --panel-brown: #6e4428;
    --wood-light: #d2ab80;
    --wood-mid: #c39366;
    --wood-dark: #b07f52;
    --title-cream: #f6e6c6;
    --step-head: #8a3a17;
    --body-text: #2e2016;
    --intro-text: #f3e7d6;
    --tip-band: #6b3b1d;
    --tip-head: #f7d79a;
    --tip-text: #f5e9d8;
    --icon-water: #8fc6e4;
    --icon-barrel: #7a4a26;
    --icon-bulb: #f3c53a;
  }
  * { box-sizing: border-box; margin: 0; padding: 0; }
  html, body { width: 910px; height: 1200px; overflow: hidden; background: var(--page); }
  body { position: relative; font-family: "Open Sans", Arial, sans-serif; color: var(--body-text); }

  .card { position: absolute; left: 38px; width: 835px; overflow: hidden;
    background: linear-gradient(100deg, var(--wood-light) 0%, var(--wood-mid) 45%, var(--wood-light) 70%, var(--wood-dark) 100%);
    box-shadow: 0 2px 6px rgba(0,0,0,.25); }
  .card--front { top: 23px; height: 549px; }
  .card--back { top: 610px; height: 552px; }

  .intro-panel { position: absolute; left: 0; top: 0; width: 294px; height: 100%;
    background: var(--panel-brown); padding: 31px 12px 0 13px; }
  .intro-title { font-family: "Oswald", Impact, sans-serif; font-weight: 600; color: var(--title-cream);
    font-size: 27px; line-height: 38px; text-align: center; text-transform: uppercase; white-space: nowrap; }
  .intro-text { margin-top: 26px; color: var(--intro-text); font-size: 15.5px; line-height: 24.5px; }
  .intro-text + .intro-text { margin-top: 24px; }

  .step { position: absolute; }
  .step-head { font-family: "Oswald", Impact, sans-serif; font-weight: 500; color: var(--step-head);
    font-size: 18px; text-transform: uppercase; line-height: 22px; }
  .step-body { font-size: 15.5px; line-height: 24.5px; margin-top: 2px; }

  .step-art { position: absolute; border-radius: 10px; }
  .art-water { background: linear-gradient(180deg, var(--icon-water), #5c9ec4); }
  .art-barrel { background: radial-gradient(ellipse at center, #9a6236 0%, var(--icon-barrel) 70%, #4e2c14 100%); border-radius: 40%; }
  .art-tub { background: linear-gradient(180deg, #eef6fa, #bcd6e4); border-radius: 8px 8px 22px 22px; }

  .tip-band { position: absolute; left: 0; bottom: 0; width: 100%; height: 112px;
    background: var(--tip-band); padding: 10px 20px 0 119px; color: var(--tip-text); }
  .tip-bulb { position: absolute; left: 30px; top: 22px; width: 64px; height: 64px; border-radius: 50%;
    background: radial-gradient(circle, var(--icon-bulb) 0%, #e09a22 100%); }
  .tip-head { font-family: "Oswald", Impact, sans-serif; font-weight: 500; font-size: 17px; line-height: 22px; text-transform: uppercase; color: var(--tip-head); }
  .tip-text { font-size: 15px; line-height: 24px; }
</style>
</head>
<body>

<section class="card card--front">
  <div class="intro-panel">
    <h1 class="intro-title">A Step by Step Guide<br>on How to Cure<br>Your Oak Barrel</h1>
    <p class="intro-text">First, we would like to thank you for choosing Harbor Crest Barrels for your home spirit and wine-aging needs. We know you are very excited to use it and so are we.</p>
    <p class="intro-text">However, your barrel is NOT ready yet for use. You need to cure it first to get rid of the wood debris and make it watertight. Do not fret, we laid out an easy to follow step by step guide on how to ready your barrel for spirit and wine-aging.</p>
  </div>

  <div class="step-art art-water" style="left:330px;top:34px;width:105px;height:72px" role="img" aria-label="Wooden spigot and plug soaking in water"></div>
  <div class="step" style="left:484px;top:40px;width:340px">
    <h2 class="step-head">Step 1</h2>
    <p class="step-body">Rinse and soak the spigot (wooden faucet) and the plug (or bung) in water for about half an hour.</p>
  </div>

  <div class="step-art art-barrel" style="left:336px;top:200px;width:105px;height:94px" role="img" aria-label="Half-filled barrel being shaken"></div>
  <div class="step" style="left:484px;top:171px;width:340px">
    <h2 class="step-head">Step 2</h2>
    <p class="step-body">While waiting, fill the barrel with water until it is half-full. Use your thumb to plug the holes, give it a good shake to get rid of wood chips and debris that might be trapped inside. Let the water out. You may repeat this process three to five times until you satisfied the barrel is thoroughly clean.</p>
  </div>

  <div class="step-art art-barrel" style="left:330px;top:412px;width:111px;height:92px" role="img" aria-label="Barrel with spigot fitted by hand, no hammer"></div>
  <div class="step" style="left:484px;top:422px;width:340px">
    <h2 class="step-head">Step 3</h2>
    <p class="step-body">Plug the barrel with the spigot. You may tighten it securely with your hand. We advise not to use a hammer as it may crack the wood.</p>
  </div>
</section>

<section class="card card--back">
  <div class="step-art art-tub" style="left:25px;top:33px;width:110px;height:48px" role="img" aria-label="Bathtub"></div>
  <div class="step" style="left:173px;top:29px;width:640px">
    <h2 class="step-head">Step 4</h2>
    <p class="step-body" style="margin-left:7px;margin-top:6px">Place the barrel in a sink, tub, or any place that is OK to get wet.</p>
  </div>

  <div class="step-art art-water" style="left:25px;top:109px;width:100px;height:86px" role="img" aria-label="Hot water poured into barrel through a funnel"></div>
  <div class="step" style="left:173px;top:115px;width:640px">
    <h2 class="step-head">Step 5</h2>
    <p class="step-body">Using a funnel, fill the barrel with hot water until it is full. Leave the top hole open. Your barrel might leak, and that's OK. It is not watertight yet and this process will make the wood expand to seal the gaps.</p>
  </div>

  <div class="step-art art-barrel" style="left:35px;top:230px;width:80px;height:71px" role="img" aria-label="Filled barrel resting"></div>
  <div class="step" style="left:173px;top:234px;width:640px">
    <h2 class="step-head">Step 6</h2>
    <p class="step-body">Leave the barrel this way until no more leakages can be seen. This means the wood has expanded and the gaps are sealed. This can take from 30 minutes to an entire week, depending on the size of the barrel.</p>
  </div>

  <div class="step-art art-barrel" style="left:25px;top:326px;width:80px;height:90px" role="img" aria-label="Barrel being drained through the spigot"></div>
  <div class="step" style="left:173px;top:349px;width:640px">
    <h2 class="step-head">Step 7</h2>
    <p class="step-body">Drain the barrel and let it air dry for no more than four hours. After 4 hours, it is ready to be filled with any spirits or wine of your choice.</p>
  </div>

  <div class="tip-band">
    <div class="tip-bulb" role="img" aria-label="Light bulb"></div>
    <h2 class="tip-head">Additional Tip</h2>
    <p class="tip-text">If you plan on aging different kinds of alcohol using the same barrel, you must cure the barrel again(Step 6) for three to five days. This will allow the barrel to absorb enough water and prevent the next batch of alcohol from being contaminated.</p>
  </div>
</section>

</body>
</html>
```